Business card design for new brand

We have recently rebranded and need a new business card template.

We are an insurance underwriting agency. All of our products are sold via other partner companies, so these are just to pass on our details to other organisations.

We would like to see designs that use the colour green (current stationary generally uses lime green (rgb 142,190,63) and forest green (0,154,79) to comply with our logo's colours. We are happy with other shades of green.

Business cards need to include our logo, as well as space for:
1. Full name
2. Qualifications (optional)
3. Title
4. Office number
5. Mobile number
6. Email address

Our logo is enclosed here.

```html
<!DOCTYPE html>
<html lang="en">
<head>
<meta charset="utf-8">
<title>Coverwell business card</title>
<link rel="stylesheet" href="https://fonts.googleapis.com/css2?family=Montserrat:wght@700&family=Arimo:wght@400&display=swap">
<style>
  :root {
    --backdrop: #2b2624;
    --card: #1b1b1b;
    --green-deep: #0b6a2f;
    --green-forest: #009a4f;
    --green-lime: #8ebe3f;
    --ink: #f2f2f2;
    --rule: #bdbdbd;
  }
  * { box-sizing: border-box; margin: 0; padding: 0; }
  html, body { width: 1200px; height: 842px; overflow: hidden; }
  body {
    background: var(--backdrop);
    display: flex;
    align-items: center;
    justify-content: center;
    gap: 44px;
  }
  .card {
    position: relative;
    width: 520px;
    height: 298px;
    background: var(--card);
    box-shadow: 0 12px 30px rgba(0,0,0,.45);
    overflow: hidden;
  }
  .band {
    position: absolute;
    left: 0; right: 0;
    height: 14px;
    display: flex;
  }
  .band--top { top: 0; }
  .band--bottom { bottom: 0; }
  .band__seg--deep { flex: 37; background: var(--green-deep); }
  .band__seg--forest { flex: 33; background: var(--green-forest); }
  .band__seg--lime { flex: 30; background: var(--green-lime); }

  .contact {
    position: absolute;
    left: 0; right: 0; top: 78px;
    text-align: center;
    font-family: "Arimo", Arial, sans-serif;
    color: var(--ink);
  }
  .contact__name {
    font-family: "Montserrat", Arial, sans-serif;
    font-weight: 700;
    font-size: 26px;
    color: var(--green-forest);
    letter-spacing: .3px;
  }
  .contact__title { font-size: 17px; margin-top: 2px; }
  .contact__rule {
    width: 140px; height: 1px;
    background: var(--rule);
    margin: 14px auto 14px;
  }
  .contact__line { font-size: 17px; line-height: 1.35; }

  .brand {
    position: absolute;
    inset: 0;
    display: flex;
    align-items: center;
    justify-content: center;
    gap: 16px;
  }
  .brand__mark {
    width: 34px; height: 34px;
    background: var(--green-lime);
  }
  .brand__name {
    font-family: "Montserrat", Arial, sans-serif;
    font-weight: 700;
    font-size: 44px;
    color: var(--ink);
  }
</style>
</head>
<body>
  <section class="card card--contact">
    <div class="band band--top"><span class="band__seg--deep"></span><span class="band__seg--forest"></span><span class="band__seg--lime"></span></div>
    <div class="contact">
      <p class="contact__name">Daniel Hartley</p>
      <p class="contact__title">Managing Director</p>
      <div class="contact__rule"></div>
      <p class="contact__line">044-555 010 200</p>
      <p class="contact__line">044-555 010 200</p>
      <p class="contact__line">hello@coverwell.example</p>
    </div>
    <div class="band band--bottom"><span class="band__seg--deep"></span><span class="band__seg--forest"></span><span class="band__seg--lime"></span></div>
  </section>

  <section class="card card--brand">
    <div class="band band--top"><span class="band__seg--deep"></span><span class="band__seg--forest"></span><span class="band__seg--lime"></span></div>
    <div class="brand">
      <span class="brand__mark"></span>
      <span class="brand__name">Coverwell</span>
    </div>
    <div class="band band--bottom"><span class="band__seg--deep"></span><span class="band__seg--forest"></span><span class="band__seg--lime"></span></div>
  </section>
</body>
</html>
```